Site Design - PSD Only - festival management

We are looking for a final design for our B2B marketplace. The project is a social commerce platform managing the application and transaction process for festivals and local events. The site design should be based on either Bootstrap or Zurb Foundation. We will provide logos and example images.

Two of the most critical pages will be the home page and the search interface, as well several dashboards. Beyond that, most of the pages will be standard forms and other typical pages that drop into the general site theme. The design tends towards minimalism to simplify the UX and speed up the interface. It incorporates elements from the the following websites. Although the wireframes may lift design elements directly from some of these sites, we are looking for a design that incorporates them more as inspiration.

quilo.co - good example of minimalist structure on internal pages
ravtorn.com - some similarities on search pages, etc.
vexdal.com - nice simple layout for features on home and internal pages
mossbrackle.com - nice alternative to standard bootstrap template

We're nearing the end of this project.  I've received some good submissions , but they are all variations on the exact same theme.  I would still like to see something that doesn't look like a bootstrap template.  I suggested the following idea to a few of the submitters, but now I am adding it to the main project description in hopes of stoking the engine.

The idea I had is for something a little less "bootstrappy" riffs on the design at mossbrackle.com with a flat background color that nicely offsets the blue in the logo. Rather than pulling in a stock image I thought about creating a derivation of the iconic Harrowmere poster, perhaps with vendor tents as tuning pegs and a silhouette of people on the neck. Just throwing that out there. 

I'm not a designer, though, so here's hoping we can see some different ideas while the project is still open.

Thanks.

Target Market(s)

Target market: Festival and event organizers; event participants including exhibitors, vendors, musicians, authors, volunteers, etc.

Industry/Entity Type

Festival

Requirements
Must have
• Home page, Search page, User dash, Organization dash, Event dash, Features, FAQ, various forms
Nice to have
• Would like to see some alternative designs to the standard bootstrap templates...creativity is encouraged.
Should not have
• Should not look like it was pulled off of the shelf.

```html
<!DOCTYPE html>
<html lang="en">
<head>
<meta charset="utf-8">
<title>Festara – Festival Management</title>
<link href="https://fonts.googleapis.com/css2?family=Oxygen:wght@400;700&family=Passion+One&display=swap" rel="stylesheet">
<style>
:root{
  --blue:#2a80c4;
  --blue-dark:#1c64a4;
  --text:#333;
  --muted:#8a8a8a;
  --line:#e3e3e3;
  --footer-light:#f3f3f3;
  --footer-dark:#2b2b2b;
  --icon-grey:#8c8c8c;
}
*{margin:0;padding:0;box-sizing:border-box}
html,body{width:952px;height:1200px;overflow:hidden;background:#fff;font-family:'Oxygen',sans-serif;color:var(--text)}
.page{position:relative;width:952px;height:1200px}

/* header */
.site-header{position:absolute;left:0;top:0;width:952px;height:99px;background:linear-gradient(#fff,#f6f6f6);border-bottom:1px solid var(--line)}
.brand{position:absolute;left:79px;top:30px;display:flex;align-items:center;gap:8px}
.brand-dot{width:26px;height:26px;border-radius:50%;background:var(--blue)}
.brand-name{font-size:27px;font-weight:400;color:#3c3c3c;letter-spacing:1px}
.actions{position:absolute;left:257px;top:0;display:flex;height:86px}
.action{width:87px;padding:13px 0 0 15px;border-left:1px solid var(--line);font-size:10px;line-height:15px;color:#555}
.action:last-child{border-right:1px solid var(--line)}
.action b{display:block;font-weight:400;font-size:12px;color:var(--blue);margin-bottom:3px}
.search{position:absolute;left:642px;top:18px;width:159px;height:25px;border:1px solid #cfcfcf;background:#fff;font-size:10px;color:#555;padding:6px 12px}
.search svg{position:absolute;right:7px;top:5px}
.social-top{position:absolute;left:815px;top:19px;display:flex;gap:9px}
.social-top span{width:24px;height:24px;border-radius:50%}
.social-top span:first-child{background:#2c4f8c}
.social-top span:last-child{background:#3ab0e6}
.main-nav{position:absolute;right:79px;top:67px;display:flex;gap:16px;font-size:10.5px;color:#555}
.main-nav .current{color:var(--blue)}
.main-nav .account{color:#111;margin-left:0}

/* hero */
.hero{position:absolute;left:0;top:99px;width:952px;height:419px;background:linear-gradient(160deg,#5d7a3c 0%,#8c7a55 30%,#c89a78 55%,#7a6a52 78%,#3c3a30 100%)}
.hero-arrow{position:absolute;top:194px;width:26px;height:26px;border-radius:50%;background:rgba(255,255,255,.55);display:flex;align-items:center;justify-content:center}
.hero-arrow.prev{left:79px}
.hero-arrow.next{left:846px}
.caption{position:absolute;left:79px;top:336px;width:794px;height:73px;background:rgba(25,25,25,.88);display:flex;align-items:center}
.caption-tag{width:138px;height:73px;background:linear-gradient(#3487c6,#1f69ab);font-family:'Passion One',sans-serif;color:#fff;font-size:30px;line-height:29px;text-align:center;padding-top:8px}
.caption-body{padding-left:15px;font-family:'Passion One',sans-serif;color:#fff}
.caption-title{font-size:19px;margin-bottom:6px}
.caption-line{font-size:15px;color:#d8d8d8;display:flex;align-items:baseline;gap:12px}
.caption-line .cta{color:#47b2f0;font-size:21px}

/* features */
.feature{position:absolute;width:266px;text-align:center}
.feature svg,.feature .icon-fill{display:block;margin:0 auto}
.feature h3{font-size:18px;font-weight:400;color:var(--blue);line-height:19px}
.feature p{font-size:12px;line-height:20px;color:var(--muted)}
.btn{position:absolute;left:92px;width:81px;height:27px;background:linear-gradient(#2d8ad0,#1a66a8);border-radius:2px;color:#fff;font-size:12px;line-height:27px;text-align:center}
.icon-fill{width:70px;height:70px;border-radius:50%;background:#d6e7f5}

/* footers */
.contact-bar{position:absolute;left:0;top:1060px;width:952px;height:62px;background:var(--footer-light);border-top:1px solid var(--line);font-size:11px;color:#666}
.contact{position:absolute;top:21px;display:flex;align-items:center;gap:9px}
.social-foot{position:absolute;left:692px;top:19px;display:flex;gap:8px}
.social-foot span{width:20px;height:20px;border-radius:50%;background:var(--icon-grey);display:flex;align-items:center;justify-content:center}
.site-footer{position:absolute;left:0;top:1122px;width:952px;height:78px;background:var(--footer-dark);color:#d0d0d0;font-size:11px;text-align:center}
.site-footer .links{margin-top:19px;word-spacing:2px}
.site-footer .copy{margin-top:10px}
</style>
</head>
<body>
<div class="page">

<header class="site-header">
  <div class="brand"><span class="brand-dot"></span><span class="brand-name">FESTARA</span></div>
  <div class="actions">
    <div class="action"><b>Apply...</b>to a festival<br>or local event</div>
    <div class="action"><b>Add...</b>your event to<br>the Festara<br>network</div>
    <div class="action"><b>Join...</b>discussions<br>with industry<br>professionals</div>
  </div>
  <div class="search">Search
    <svg width="13" height="13" viewBox="0 0 13 13"><circle cx="5" cy="5" r="3.6" fill="none" stroke="#222" stroke-width="2"/><line x1="7.6" y1="7.6" x2="12" y2="12" stroke="#222" stroke-width="2.4"/></svg>
  </div>
  <div class="social-top"><span></span><span></span></div>
  <nav class="main-nav">
    <span class="current">About us</span><span>Features</span><span>FAQ</span><span>Blog</span><span>Press</span>
    <span class="account">REGISTER &nbsp;|&nbsp; LOGIN</span>
  </nav>
</header>

<section class="hero" role="img" aria-label="Photo of a festival crowd raising their hands outdoors">
  <div class="hero-arrow prev"><svg width="10" height="10"><polyline points="7,1 3,5 7,9" fill="none" stroke="#888" stroke-width="1.5"/></svg></div>
  <div class="hero-arrow next"><svg width="10" height="10"><polyline points="3,1 7,5 3,9" fill="none" stroke="#888" stroke-width="1.5"/></svg></div>
  <div class="caption">
    <div class="caption-tag">PEACE OF<br>MIND</div>
    <div class="caption-body">
      <div class="caption-title">Welcome to Festara.</div>
      <div class="caption-line">We Connect festival and event organisers with the people that make it happen. <span class="cta">GET STARTED</span></div>
    </div>
  </div>
</section>

<!-- row one -->
<div class="feature" style="left:78px;top:551px">
  <svg width="70" height="70" viewBox="0 0 70 70" fill="none" stroke="#2a80c4" stroke-width="3"><circle cx="35" cy="35" r="33"/><ellipse cx="35" cy="35" rx="14" ry="33"/><line x1="35" y1="2" x2="35" y2="68"/><line x1="2" y1="35" x2="68" y2="35"/><path d="M7 18h56M7 52h56"/></svg>
  <h3 style="margin-top:18px">Online Applications</h3>
  <p style="margin-top:6px">Quisque laoreet metus ut nisi condi<br>mentum ullamcorper. In dapibus pel<br>lentesque metus et pulvinar.</p>
  <span class="btn" style="top:174px">Learn More</span>
</div>
<div class="feature" style="left:345px;top:551px">
  <svg width="76" height="70" viewBox="0 0 76 70" fill="none" stroke="#2a80c4" stroke-width="3"><rect x="26" y="1" width="24" height="16"/><path d="M38 17v15M10 32h56M10 32v20M38 32v20M66 32v20"/><rect x="1" y="52" width="18" height="16"/><rect x="29" y="52" width="18" height="16"/><rect x="57" y="52" width="18" height="16"/></svg>
  <h3 style="margin-top:18px">Integrated Scheduling</h3>
  <p style="margin-top:6px">Quisque laoreet metus ut nisi condi<br>mentum ullamcorper. In dapibus pel<br>lentesque metus et pulvinar.</p>
  <span class="btn" style="top:174px">Learn More</span>
</div>
<div class="feature" style="left:610px;top:551px">
  <svg width="40" height="70" viewBox="0 0 40 70" fill="none" stroke="#2a80c4" stroke-width="3"><rect x="2" y="2" width="36" height="66" rx="6"/><rect x="7" y="10" width="26" height="46" rx="2"/><circle cx="20" cy="62" r="1.5" fill="#2a80c4"/></svg>
  <h3 style="margin-top:18px">Native Phone &amp; Tablet Apps</h3>
  <p style="margin-top:6px">Quisque laoreet metus ut nisi condi<br>mentum ullamcorper. In dapibus pel<br>lentesque metus et pulvinar.</p>
  <span class="btn" style="top:174px">Learn More</span>
</div>

<!-- row two -->
<div class="feature" style="left:78px;top:807px">
  <svg width="76" height="70" viewBox="0 0 76 70" fill="none" stroke="#2a80c4" stroke-width="3"><polyline points="3,35 22,27 39,15 52,24 73,5"/><polyline points="3,62 22,64 39,49 52,62 73,43"/><g fill="#2a80c4" stroke="none"><circle cx="3" cy="35" r="3"/><circle cx="22" cy="27" r="3"/><circle cx="39" cy="15" r="3"/><circle cx="52" cy="24" r="3"/><circle cx="73" cy="5" r="3"/><circle cx="3" cy="62" r="3"/><circle cx="22" cy="64" r="3"/><circle cx="39" cy="49" r="3"/><circle cx="52" cy="62" r="3"/><circle cx="73" cy="43" r="3"/></g></svg>
  <h3 style="margin-top:21px">Real -Time Analytics</h3>
  <p style="margin-top:24px">Quisque laoreet metus ut nisi condi<br>mentum ullamcorper. In dapibus pel<br>lentesque metus et pulvinar.</p>
  <span class="btn" style="top:193px">Learn More</span>
</div>
<div class="feature" style="left:345px;top:807px">
  <svg width="74" height="74" viewBox="0 0 74 74" fill="none" stroke="#2a80c4" stroke-width="3"><circle cx="37" cy="37" r="35"/><circle cx="37" cy="29" r="12"/><path d="M15 62c3-12 12-17 22-17s19 5 22 17"/></svg>
  <h3 style="margin-top:17px">Social Network Integration</h3>
  <p style="margin-top:24px">Quisque laoreet metus ut nisi condi<br>mentum ullamcorper. In dapibus pel<br>lentesque metus et pulvinar.</p>
  <span class="btn" style="top:193px">Learn More</span>
</div>
<div class="feature" style="left:610px;top:807px">
  <div class="icon-fill" role="img" aria-label="Piggy bank icon"></div>
  <h3 style="margin-top:21px">Enhanced Sponsorship<br>Opportunities</h3>
  <p style="margin-top:5px">Quisque laoreet metus ut nisi condi<br>mentum ullamcorper. In dapibus pel<br>lentesque metus et pulvinar.</p>
  <span class="btn" style="top:193px">Learn More</span>
</div>

<section class="contact-bar">
  <div class="contact" style="left:138px">
    <svg width="22" height="22" viewBox="0 0 22 22"><path d="M3 2l5 0 2 5-3 2c2 4 4 6 7 7l2-3 5 2v5c-10 0-18-8-18-18z" fill="#8c8c8c"/></svg>
    Phone: (800) 555-0142
  </div>
  <div class="contact" style="left:401px">
    <svg width="22" height="15" viewBox="0 0 22 15"><rect width="22" height="15" fill="#9a9a9a"/><polyline points="0,0 11,8 22,0" fill="none" stroke="#fff" stroke-width="1.5"/></svg>
    E-mail : hello@festara.net
  </div>
  <div class="social-foot">
    <span></span><span></span><span></span>
    <span><svg width="11" height="8"><rect x=".5" y=".5" width="10" height="7" fill="none" stroke="#fff"/><polyline points=".5,.5 5.5,4.5 10.5,.5" fill="none" stroke="#fff"/></svg></span>
  </div>
</section>

<footer class="site-footer">
  <div class="links">Home &nbsp;|&nbsp; About us &nbsp;|&nbsp; Features &nbsp;|&nbsp; FAQ &nbsp;|&nbsp; Blog &nbsp;|&nbsp; Press &nbsp;|&nbsp; Register &nbsp;|&nbsp; Login</div>
  <div class="copy">Copyright &copy; 2013 Festara. &nbsp; All rights reserved. &nbsp; Privacy Policy &nbsp;|&nbsp; Terms and Conditions.</div>
</footer>

</div>
</body>
</html>
```